Wren Vehicle Polishing (Mobile detail)

I need a business card made up. I'd like it to be different in some form, either raised, embossed, debossed, something cool that stands out. (preferably embossed text somewhere in it). I will be including the Initial png file. Let me know if you need the photoshop of adobe illustrator file to work with.
Updates

Information to be included: Text: XXX-XXX-XXXX Phone: XXX-XXX-XXXX Email: wrenvehiclepolish@mailnest.example Website: www.socialpage.example/wrenvehiclepolishKTR Hours of operation: Mon - Fri 7:00AM to 8:00PM Sat - 10:00AM to 8:00PM

Target Market(s)

Mobile automotive detailing

Industry/Entity Type

Automotive

Contact Information for Business Card

Make it stand out with embossed lettering, I'd also like the background to be glossy black or matte, something that represents a shiny car, black preferred

Requirements
Must have
• A glossy background, or something.
• My logo, pick one of them that best fits your design.
Should not have
• White background,
• something that does not stand out.

```html
<!DOCTYPE html>
<html lang="en">
<head>
<meta charset="utf-8">
<title>Wren Vehicle Polishing – Business Card</title>
<link rel="stylesheet" href="https://fonts.googleapis.com/css2?family=Anton&family=Questrial&family=Arimo:wght@400&display=swap">
<style>
  :root {
    --ink-black: #050505;
    --panel-grey: #8a8a8a;
    --panel-grey-light: #9a9a9a;
    --accent-orange: #e8771f;
    --text-white: #ffffff;
    --mark-silver: #d9d9d9;
  }
  * { margin: 0; padding: 0; box-sizing: border-box; }
  html, body {
    width: 1200px; height: 668px; overflow: hidden;
    background: var(--ink-black);
  }
  .card {
    position: relative;
    width: 1200px; height: 668px;
    overflow: hidden;
    background: var(--ink-black);
    font-family: "Arimo", Arial, sans-serif;
  }
  .card-shapes { position: absolute; inset: 0; }
  .brand-title {
    position: absolute;
    left: 530px; top: 60px; width: 650px;
    text-align: center;
    font-family: "Anton", "Impact", sans-serif;
    font-size: 64px; line-height: 1;
    color: var(--accent-orange);
    letter-spacing: 0.5px;
    text-transform: uppercase;
    transform: scaleY(1.75);
    transform-origin: top center;
    white-space: nowrap;
  }
  .role {
    position: absolute;
    left: 684px; top: 290px;
    font-family: "Questrial", "Century Gothic", sans-serif;
    font-size: 48px; line-height: 1;
    color: var(--accent-orange);
  }
  .role-reflection {
    position: absolute;
    left: 684px; top: 340px;
    font-family: "Questrial", "Century Gothic", sans-serif;
    font-size: 48px; line-height: 1;
    color: var(--accent-orange);
    transform: scaleY(-0.45);
    transform-origin: top left;
    opacity: 0.3;
  }
  .contact-list { position: absolute; left: 44px; top: 418px; list-style: none; }
  .contact-item {
    display: flex; align-items: center;
    height: 50px;
    color: var(--text-white);
    font-size: 23px;
  }
  .contact-icon { width: 40px; height: 40px; margin-right: 37px; flex: none; }
  .hours {
    position: absolute; left: 46px; top: 570px;
    color: var(--text-white);
    font-size: 20px; line-height: 27px;
  }
  .brand-mark {
    position: absolute; left: 885px; top: 470px;
    width: 190px;
    display: flex; flex-direction: column; align-items: center;
    text-align: center;
    font-family: "Questrial", sans-serif;
    font-size: 24px; line-height: 1.1;
    color: var(--mark-silver);
  }
  .brand-mark-dot {
    width: 70px; height: 70px; border-radius: 50%;
    background: var(--accent-orange);
    margin-bottom: 10px;
  }
  .brand-watermark {
    position: absolute; left: 200px; top: 130px;
    width: 430px;
    display: flex; flex-direction: column; align-items: center;
    font-family: "Questrial", sans-serif;
    font-size: 52px; line-height: 1.05; text-align: center;
    color: var(--text-white);
    opacity: 0.08;
  }
  .brand-watermark-dot {
    width: 150px; height: 150px; border-radius: 50%;
    background: var(--text-white);
    margin-bottom: 18px;
  }
</style>
</head>
<body>
<div class="card">
  <svg class="card-shapes" width="1200" height="668" viewBox="0 0 1200 668" aria-hidden="true">
    <path class="title-pill" d="M620 0 H1200 V255 H610 A128 128 0 0 1 482 127 A128 128 0 0 1 610 0 Z" fill="var(--panel-grey)"/>
    <path class="contact-band" d="M0 402 H480 C560 402 590 463 680 463 H1200 V668 H0 Z" fill="var(--panel-grey)"/>
  </svg>

  <div class="brand-watermark" aria-hidden="true">
    <span class="brand-watermark-dot"></span>
    Wren Vehicle Polishing
  </div>

  <h1 class="brand-title">Wren Vehicle Polishing</h1>

  <p class="role">Project Owner</p>
  <p class="role-reflection" aria-hidden="true">Project Owner</p>

  <ul class="contact-list">
    <li class="contact-item">
      <svg class="contact-icon" viewBox="0 0 40 40" aria-hidden="true">
        <path d="M4 14 C4 6 36 6 36 14 V17 H28 V13 H12 V17 H4 Z" fill="var(--text-white)"/>
        <path d="M11 18 H29 L34 34 H6 Z" fill="var(--text-white)"/>
        <circle cx="20" cy="26" r="4" fill="var(--panel-grey)"/>
      </svg>
      <span>XXX-XXX-XXXX</span>
    </li>
    <li class="contact-item">
      <svg class="contact-icon" viewBox="0 0 40 40" aria-hidden="true">
        <rect x="3" y="9" width="34" height="23" fill="none" stroke="var(--text-white)" stroke-width="2"/>
        <path d="M3 9 L20 23 L37 9 M3 32 L15 19 M37 32 L25 19" fill="none" stroke="var(--text-white)" stroke-width="2"/>
      </svg>
      <span>wrenvehiclepolish@mailnest.example</span>
    </li>
    <li class="contact-item">
      <svg class="contact-icon" viewBox="0 0 40 40" aria-hidden="true">
        <rect x="4" y="4" width="32" height="32" fill="var(--text-white)"/>
      </svg>
      <span>www.socialpage.example/wrenvehiclepolishKTR</span>
    </li>
  </ul>

  <p class="hours">Hours of operation:<br>Mon - Fri 7:00AM to 8:00PM Sat - 10:00AM to 8:00PM</p>

  <div class="brand-mark">
    <span class="brand-mark-dot"></span>
    Wren Vehicle Polishing
  </div>
</div>
</body>
</html>
```